Modern brochure by Lawyers, for modern clients

It'sa "News" for their clients. Attached you can find the current News without design. It must be elegant but very attractive and modern. Their web site is http://www.montealtoyasociados.cl/ Their expertise is labor and employment practice area. It must be in editable format so that lawyers can write the news in a template with this corporate design.

Target Market(s)

Big Companies

Font styles to use
Sans Serif

Colors
0255a3
474747

Requirements
Nice to have
• Legal Pictures and only a little of yellow. One touch! It must be in editable format so that lawyers can write the news in a template with this corporate design.

```html
<!DOCTYPE html>
<html lang="es">
<head>
<meta charset="utf-8">
<title>Montealto &amp; Asociados Abogados — Noticias</title>
<link href="https://fonts.googleapis.com/css2?family=Cabin:wght@400;500;600&display=swap" rel="stylesheet">
<style>
  :root {
    --brand-blue: #0255a3;
    --ink: #474747;
    --navy: #1f3a68;
    --accent-yellow: #f2e200;
    --backdrop: #9ea3ab;
    --paper: #ffffff;
    --footer-bg: #eef1f6;
    --rule: #e3e6ea;
  }
  * { box-sizing: border-box; margin: 0; padding: 0; }
  html, body { width: 1200px; height: 947px; overflow: hidden; }
  body {
    background: var(--backdrop);
    font-family: "Cabin", Arial, sans-serif;
    color: var(--ink);
    display: flex;
    align-items: center;
    justify-content: center;
  }
  .newsletter {
    width: 640px;
    height: 917px;
    background: var(--paper);
    position: relative;
    display: flex;
    flex-direction: column;
    box-shadow: 0 6px 24px rgba(0,0,0,.18);
    border-top: 3px solid var(--accent-yellow);
    border-bottom: 3px solid var(--brand-blue);
  }
  .hero-band {
    height: 88px;
    background: linear-gradient(90deg, #a9a189 0%, #c9c2ae 35%, #bdb8a8 65%, #a8a698 100%);
  }
  .masthead {
    display: flex;
    justify-content: space-between;
    align-items: center;
    padding: 26px 52px 22px 50px;
    border-bottom: 1px solid var(--rule);
  }
  .brand { display: flex; align-items: center; gap: 10px; }
  .brand-dot { width: 34px; height: 34px; border-radius: 50%; background: var(--navy); }
  .brand-name {
    font-size: 24px; font-weight: 400; color: var(--navy);
    line-height: 1.05; letter-spacing: .5px; width: 200px;
    border-right: 3px solid var(--navy); padding-right: 8px;
  }
  .issue-date { text-align: right; color: var(--brand-blue); font-weight: 600; font-size: 16px; line-height: 1.35; }
  .issue-date svg { display: block; margin: 0 0 8px auto; }
  .article { padding: 76px 52px 0 50px; flex: 1; font-size: 14.5px; line-height: 1.5; }
  .greeting { color: var(--brand-blue); font-weight: 600; font-size: 15px; margin-bottom: 18px; }
  .article p { margin-bottom: 22px; }
  .article a { color: var(--brand-blue); font-style: italic; }
  .signoff { margin-top: 4px; }
  .sender {
    background: var(--footer-bg);
    height: 96px;
    display: flex;
    align-items: center;
    padding: 0 40px;
    gap: 14px;
  }
  .sender-portrait {
    width: 46px; height: 46px; border-radius: 50%;
    background: linear-gradient(#5b6573, #2c333d);
    border: 3px solid var(--brand-blue);
  }
  .sender-name { color: var(--brand-blue); font-weight: 600; font-size: 15px; }
  .sender-mail { display: flex; align-items: center; gap: 6px; font-size: 13px; margin-top: 4px; }
  .sender-mark { margin-left: auto; display: flex; align-items: center; gap: 6px; color: var(--navy); font-size: 11px; opacity: .8; }
  .sender-mark span.dot { width: 12px; height: 12px; border-radius: 50%; background: var(--navy); }
</style>
</head>
<body>
  <article class="newsletter">
    <div class="hero-band" role="img" aria-label="Fotografía de profesionales caminando vistos desde arriba"></div>

    <header class="masthead">
      <div class="brand">
        <span class="brand-dot"></span>
        <div class="brand-name">Montealto &amp; Asociados Abogados</div>
      </div>
      <div class="issue-date">
        <svg width="30" height="30" viewBox="0 0 30 30" aria-hidden="true">
          <circle cx="15" cy="15" r="15" fill="#0255a3"/>
          <rect x="8" y="9" width="14" height="13" rx="1" fill="none" stroke="#fff" stroke-width="1.6"/>
          <line x1="8" y1="12.5" x2="22" y2="12.5" stroke="#fff" stroke-width="1.6"/>
          <g fill="#fff"><rect x="10" y="14.5" width="2" height="2"/><rect x="14" y="14.5" width="2" height="2"/><rect x="18" y="14.5" width="2" height="2"/><rect x="10" y="18" width="2" height="2"/><rect x="14" y="18" width="2" height="2"/></g>
        </svg>
        Santiago,<br>25 de julio de 2018
      </div>
    </header>

    <section class="article">
      <p class="greeting">Estimados,</p>
      <p>Por medio del presente, les damos a conocer el Dictamen Ordinario N° 3826-031, emitido por la Dirección del Trabajo el pasado 20 de julio, relativo a los “beneficios históricos”.</p>
      <p>Estos fueron definidos en su oportunidad por este organismo como “…aquellos beneficios que se han otorgado desde siempre…” por parte del empleador.</p>
      <p>A partir de este Dictamen, el cual reconsidera el criterio del anterior Director del Trabajo, los beneficios históricos vuelven a ser patrimonio de la empresa y de los trabajadores que los han recibido, dejando de serlo de la organización sindical y de sus socios beneficiados por el solo hecho de haberse “replicado” en un instrumento colectivo durante una negociación.</p>
      <p>Por último, el Dictamen en comento aclara que si un “beneficio histórico” se incrementa de manera real y efectiva producto de una negociación colectiva, únicamente dicho incremento se entenderá originado en el respectivo instrumento colectivo, y en consecuencia, objeto de una posible extensión en el evento de que ésta se haya acordado durante la negociación.</p>
      <p>Para mayor análisis de lo resuelto por la Dirección del Trabajo, se puede revisar el Dictámen en comento haciendo <a href="http://www.montealtoyasociados.cl/">click aquí</a></p>
      <p class="signoff">Sin otro particular, saluda atentamente a ustedes,</p>
    </section>

    <footer class="sender">
      <div class="sender-portrait" role="img" aria-label="Retrato del abogado remitente"></div>
      <div>
        <div class="sender-name">Montealto &amp; Asoc. Abogados</div>
        <div class="sender-mail">
          <svg width="14" height="14" viewBox="0 0 14 14" aria-hidden="true">
            <circle cx="7" cy="7" r="7" fill="#0255a3"/>
            <rect x="3.5" y="4.5" width="7" height="5" fill="none" stroke="#fff" stroke-width="1"/>
            <polyline points="3.5,4.5 7,7.5 10.5,4.5" fill="none" stroke="#fff" stroke-width="1"/>
          </svg>
          oficina@montealtoyasociados.cl
        </div>
      </div>
      <div class="sender-mark"><span class="dot"></span>Montealto &amp; Asociados</div>
    </footer>
  </article>
</body>
</html>
```